A3 Poster & DL Flyer Design Project

We need a poster and flyer designed to advertise a Wine, Food and Live music event.
Event title is "An Evening Under Vines" and is put on by Holloway's Ridge Wines. Date for the event is Sunday 21 April 2013
The outdoor event covers wine, gourmet food and live music
Live music genera is Jazz, Blues, Swing

Reason: Most of the designs did not meet our requirements only 3 out of 21 have potential but would like to see more

Target Market(s)

25 - 55 wine drinkers with money.

Industry/Entity Type

Event

Requirements
Must have
• Title of the Event "An Evening Under Vinez"
Date Sunday 21 April 2013 or be generic where we can write the date on each year.
Camel Logo
Entry is Free
No BYO Alcohol
Must reflect Wine, Food & Live Music

```html
<!DOCTYPE html>
<html lang="en">
<head>
<meta charset="utf-8">
<title>An Evening Under Vinez — Holloway's Ridge Wines</title>
<link href="https://fonts.googleapis.com/css2?family=Arimo:wght@400&family=Pinyon+Script&display=swap" rel="stylesheet">
<style>
  :root {
    --royal: #065ea6;
    --royal-deep: #0a4f8e;
    --slate: #4d4949;
    --teal: #6697aa;
    --ink: #2a2a2a;
    --silhouette: #111111;
    --paper: #ffffff;
    --mist: #c9d6f2;
    --sky: #9fb6e8;
  }
  * { box-sizing: border-box; margin: 0; padding: 0; }
  html, body { width: 848px; height: 1200px; overflow: hidden; background: var(--paper); }
  .poster {
    position: relative; width: 848px; height: 1200px; overflow: hidden;
    font-family: "Arimo", Arial, sans-serif; background: var(--paper);
  }
  .header { position: absolute; inset: 0 0 auto 0; height: 283px; background: var(--paper); }
  .event-mark {
    position: absolute; left: 55px; top: 85px; width: 268px; height: 147px;
    background: linear-gradient(180deg, #2b2b2b 0%, var(--silhouette) 100%);
    border-radius: 4px;
  }
  .winery {
    position: absolute; left: 455px; top: 73px; width: 351px; height: 150px;
    display: flex; flex-direction: column; align-items: flex-end; justify-content: flex-end;
    gap: 0;
  }
  .winery-square { width: 101px; height: 101px; background: var(--teal); margin-bottom: 24px; }
  .winery-name {
    font-size: 19px; letter-spacing: 2.6px; color: var(--ink); text-transform: uppercase;
    white-space: nowrap;
  }
  .title-band {
    position: absolute; left: 0; top: 283px; width: 848px; height: 301px; background: var(--royal);
    color: var(--paper);
  }
  .title-lead { position: absolute; left: 64px; top: 42px; font-size: 51px; line-height: 1; }
  .title-main {
    position: absolute; left: 26px; top: 62px; width: 800px;
    font-family: "Pinyon Script", cursive; font-size: 132px; line-height: 1.4;
    white-space: nowrap; text-align: center;
  }
  .date-band {
    position: absolute; left: 0; top: 584px; width: 848px; height: 69px; background: var(--slate);
    color: var(--paper); font-size: 32px; display: flex; align-items: center; justify-content: center;
    padding-right: 30px;
  }
  .feature-field {
    position: absolute; left: 0; top: 653px; width: 848px; height: 547px;
    background:
      radial-gradient(ellipse 340px 300px at 60px 120px, var(--sky) 0%, rgba(159,182,232,0) 100%),
      radial-gradient(ellipse 300px 260px at 120px 420px, var(--mist) 0%, rgba(201,214,242,0) 100%),
      radial-gradient(ellipse 260px 200px at 420px 110px, #e2e8f8 0%, rgba(226,232,248,0) 100%),
      linear-gradient(100deg, #bccbf0 0%, #e6ecfa 45%, var(--paper) 80%);
  }
  .highlights { position: absolute; left: 0; top: 0; width: 848px; height: 547px; }
  .highlight {
    position: absolute; height: 64px; border-radius: 32px; background: var(--royal);
    color: var(--paper); font-size: 29px; display: flex; align-items: center; padding-left: 30px;
    transform: rotate(-2.2deg); transform-origin: left center;
    box-shadow: 0 6px 8px rgba(20, 40, 90, 0.35);
  }
  .highlight--entry { left: 26px; top: 135px; width: 747px; }
  .highlight--byo { left: 52px; top: 209px; width: 747px; }
  .highlight--theme { left: 76px; top: 283px; width: 744px; }
  .footer-wave { position: absolute; left: 0; bottom: 0; width: 848px; height: 80px; }
</style>
</head>
<body>
<main class="poster">
  <header class="header">
    <div class="event-mark" role="img" aria-label="Event emblem: silhouette of a traveller leading a camel"></div>
    <div class="winery">
      <div class="winery-square"></div>
      <p class="winery-name">Holloway's Ridge Wines</p>
    </div>
  </header>

  <section class="title-band">
    <p class="title-lead">An Evening</p>
    <h1 class="title-main">Under Vinez</h1>
  </section>

  <p class="date-band">Date : Sunday&nbsp; 21 April 2013</p>

  <section class="feature-field" role="img" aria-label="Soft blue background of glassy globes">
    <ul class="highlights">
      <li class="highlight highlight--entry">Entry is Free</li>
      <li class="highlight highlight--byo">No BYO Alcohol</li>
      <li class="highlight highlight--theme">Must reflect Wine, Food &amp; Live Music</li>
    </ul>
    <svg class="footer-wave" viewBox="0 0 848 80" preserveAspectRatio="none" aria-hidden="true">
      <path d="M0 64 C 260 58, 560 46, 848 20 L848 80 L0 80 Z" fill="#7fa6d6"/>
      <path d="M0 70 C 280 66, 580 54, 848 32 L848 80 L0 80 Z" fill="var(--royal)"/>
    </svg>
  </section>
</main>
</body>
</html>
```